Brightmere Skills Academy UI/UX - Responsive Design

Email squeeze page landing page design for free video training. Current website: https://www.brightmereskillsacademy.example

Website Design Brief: https://sheets.pelworthdocs.example/d/7QwPzRtYvBnMkLsDfGhJ2aXcVb9NeUoI4TyRpWq_K3/edit?usp=sharing

1 page

Font styles to use
Sans Serif

Requirements
Nice to have
• Lots of white space, clear CTA, Web3 design principles, muted colors, highly credible, trustworthy desig.

```html
<!DOCTYPE html>
<html lang="en">
<head>
<meta charset="utf-8">
<title>Brightmere Skills Academy – Free Training Sign-up</title>
<link rel="stylesheet" href="https://fonts.googleapis.com/css2?family=Montserrat:wght@400;500;600&family=Poppins:wght@600&display=swap">
<style>
  :root {
    --page-bg: #d8d8d8;
    --card-bg: #ffffff;
    --ink: #1c1c1c;
    --ink-soft: #2a2a2a;
    --muted: #8a8a8a;
    --rule: #3a3a3a;
    --brand-green: #12b512;
    --brand-green-light: #7fd97f;
    --photo-pink: #eea3ad;
    --photo-pink-deep: #e8939f;
  }
  * { box-sizing: border-box; margin: 0; padding: 0; }
  html, body { width: 1200px; height: 818px; overflow: hidden; }
  body {
    position: relative;
    background: var(--page-bg);
    font-family: "Montserrat", Arial, sans-serif;
    color: var(--ink);
  }
  .signup-card {
    position: absolute;
    left: 87px; top: 78px;
    width: 1026px; height: 660px;
    background: var(--card-bg);
    box-shadow: 0 2px 10px rgba(0,0,0,0.06);
  }
  .close-button {
    position: absolute;
    left: 1000px; top: 22px;
    font-size: 21px;
    font-weight: 400;
    color: var(--ink);
    line-height: 1;
  }
  .brand {
    position: absolute;
    left: 60px; top: 42px;
    display: flex;
    align-items: flex-start;
    gap: 16px;
  }
  .brand-mark {
    width: 48px; height: 48px;
    background: var(--brand-green);
    margin-top: 4px;
  }
  .brand-name {
    font-size: 30px;
    font-weight: 400;
    color: var(--ink);
    line-height: 1.2;
    letter-spacing: 0.2px;
  }
  .brand-tagline {
    font-size: 15.5px;
    font-weight: 500;
    color: var(--brand-green);
    margin-top: 4px;
  }
  .headline {
    position: absolute;
    left: 60px; top: 155px;
    font-family: "Poppins", Arial, sans-serif;
    font-weight: 600;
    font-size: 32px;
    line-height: 45px;
    color: var(--ink);
  }
  .intro {
    position: absolute;
    left: 63px; top: 312px;
    font-size: 19.5px;
    font-weight: 400;
    line-height: 33px;
    color: var(--ink-soft);
  }
  .email-field {
    position: absolute;
    left: 55px; top: 478px;
    width: 411px;
  }
  .email-label {
    display: flex;
    align-items: center;
    gap: 12px;
    font-size: 18px;
    font-weight: 500;
  }
  .email-label svg { width: 27px; height: 18px; }
  .email-input {
    margin-top: 13px;
    padding: 0 0 8px 39px;
    font-size: 17px;
    color: var(--muted);
    border-bottom: 1.5px solid var(--rule);
  }
  .subscribe-button {
    position: absolute;
    left: 55px; top: 568px;
    width: 411px; height: 49px;
    border-radius: 25px;
    background: var(--brand-green);
    color: #fff;
    font-size: 15px;
    font-weight: 600;
    letter-spacing: 0.3px;
    display: flex;
    align-items: center;
    justify-content: center;
  }
  .hero-photo {
    position: absolute;
    left: 559px; top: 111px;
    width: 404px; height: 415px;
    background: linear-gradient(160deg, var(--photo-pink) 0%, var(--photo-pink-deep) 100%);
  }
</style>
</head>
<body>
  <main class="signup-card">
    <div class="close-button">X</div>

    <header class="brand">
      <div class="brand-mark"></div>
      <div class="brand-text">
        <div class="brand-name">Brightmere Skills Academy</div>
        <div class="brand-tagline">Learn Today, Lead Tomorrow</div>
      </div>
    </header>

    <h1 class="headline">Sign-ups for free training<br>as precursor to Masterclass<br>sign-up for $649</h1>

    <p class="intro">Are you ready to dive into the world of<br>Artificial Intelligence and revolutionize<br>your career? Subscribe to Us and get<br>exclusive updates</p>

    <div class="email-field">
      <div class="email-label">
        <svg viewBox="0 0 27 18" aria-hidden="true">
          <rect x="0" y="0" width="27" height="18" fill="#12b512"/>
          <polyline points="1,1 13.5,10 26,1" fill="none" stroke="#ffffff" stroke-width="2"/>
        </svg>
        <span>Email</span>
      </div>
      <div class="email-input">info@harlowpenfield.example</div>
    </div>

    <div class="subscribe-button">SUBSCRIBE NOW</div>

    <div class="hero-photo" role="img" aria-label="Photo of a smiling student holding colourful notebooks and pointing towards the sign-up form, on a pink backdrop"></div>
  </main>
</body>
</html>
```